Australian Civil Construction, Quarry & Mining Services needs a business card

We need a business card designed for our Civil Construction, Quarry & Mining Services based in the country in Australia.
Our Company Brindle Earthworks provide innovate solutions for infrastructure, agricultural and mining (aggregate, sand, roadbase) industry.
We would like our business cards to be double sided
Front of card: black background or something that resembles our business colours. (it doesn't have to be black we are open to options)
- Company name - Brindle Earthworks
- Either our logo or some sort of icon/picture that resembles our business
- Website - https://brindleearthworks-example.com.au/
- We will have a number of different names, positions descriptions, phone numbers and emails on separate cards for each of our managers/directors

```html
<!DOCTYPE html>
<html lang="en">
<head>
<meta charset="utf-8">
<title>Brindle Earthworks – Business Card</title>
<link href="https://fonts.googleapis.com/css2?family=Montserrat:wght@400;500;700;800;900&display=swap" rel="stylesheet">
<style>
  :root {
    --page: #1f1f21;
    --card: #262424;
    --orange: #f07d1c;
    --white: #ffffff;
    --ink: #1b1a1a;
    --rule: #5a5656;
  }
  * { box-sizing: border-box; margin: 0; padding: 0; }
  html, body { width: 1200px; height: 800px; overflow: hidden; }
  body {
    background: var(--page);
    font-family: "Montserrat", Arial, sans-serif;
    display: flex;
    flex-direction: column;
    align-items: center;
    justify-content: center;
    gap: 30px;
  }
  .card {
    position: relative;
    width: 620px;
    height: 354px;
    background: var(--card);
    border-radius: 22px;
    overflow: hidden;
    color: var(--white);
  }
  .card__bands { position: absolute; inset: 0; width: 100%; height: 100%; }

  .brand {
    position: absolute;
    display: flex;
    align-items: center;
    gap: 12px;
    font-weight: 800;
    color: var(--orange);
    text-transform: uppercase;
    line-height: 1.05;
  }
  .brand__square { width: 30px; height: 30px; background: var(--orange); flex: none; }

  .services .brand { left: 44px; top: 132px; font-size: 24px; }
  .services__list { position: absolute; left: 340px; top: 46px; width: 250px; list-style: none; }
  .services__tag {
    display: inline-block;
    background: var(--orange);
    color: var(--ink);
    font-weight: 900;
    font-size: 17px;
    padding: 5px 18px 5px 12px;
    margin-bottom: 10px;
    text-transform: uppercase;
  }
  .services__item {
    display: flex; align-items: center; gap: 10px;
    font-weight: 800; font-size: 12.5px; text-transform: uppercase;
    padding: 7px 0;
    border-bottom: 1px solid var(--rule);
  }
  .services__bullet { width: 10px; height: 10px; background: var(--orange); flex: none; }

  .web {
    position: absolute;
    right: 26px;
    height: 44px;
    bottom: 0;
    display: flex; align-items: center; gap: 8px;
    font-weight: 800; font-size: 12px; color: var(--ink); text-transform: uppercase;
    white-space: nowrap;
  }
  .services .web { height: 50px; }

  .contact .wordmark {
    position: absolute; left: 40px; top: 42px;
    font-weight: 900; font-size: 40px; line-height: 0.95;
    color: var(--white); text-transform: uppercase;
  }
  .contact .brand { right: 40px; top: 46px; font-size: 18px; }
  .person { position: absolute; left: 40px; top: 160px; }
  .person__name { font-weight: 900; font-size: 22px; color: var(--orange); text-transform: uppercase; }
  .person__role { font-weight: 800; font-size: 13px; text-transform: uppercase; margin-top: 2px; }
  .person__lines { list-style: none; margin-top: 12px; }
  .person__line { display: flex; align-items: center; gap: 10px; font-size: 13px; font-weight: 500; padding: 2px 0; }
  .person__line svg { flex: none; }
  .address {
    position: absolute; right: 40px; top: 150px;
    display: flex; align-items: flex-start; gap: 10px;
    text-align: right; font-size: 13px; font-weight: 500; line-height: 1.4;
  }
</style>
</head>
<body>

<section class="card services" aria-label="Card back – services">
  <svg class="card__bands" viewBox="0 0 620 354" aria-hidden="true">
    <path d="M236 354 L268 304 L620 304 L620 354 Z" fill="var(--orange)"/>
  </svg>
  <div class="brand"><span class="brand__square"></span><span>Brindle<br>Earthworks</span></div>
  <ul class="services__list">
    <li class="services__tag">Our Services</li>
    <li class="services__item"><span class="services__bullet"></span>Civil Works</li>
    <li class="services__item"><span class="services__bullet"></span>Quarries Across VIC and NSW</li>
    <li class="services__item"><span class="services__bullet"></span>Crushing and Screening</li>
    <li class="services__item"><span class="services__bullet"></span>Truck and Dogs</li>
  </ul>
  <div class="web">
    <svg width="14" height="14" viewBox="0 0 16 16" aria-hidden="true"><g fill="none" stroke="var(--ink)" stroke-width="1.5"><circle cx="8" cy="8" r="6.5"/><ellipse cx="8" cy="8" rx="3" ry="6.5"/><path d="M1.5 8h13"/></g></svg>
    brindleearthworks-example.com.au
  </div>
</section>

<section class="card contact" aria-label="Card front – contact">
  <svg class="card__bands" viewBox="0 0 620 354" aria-hidden="true">
    <path d="M0 344 L222 344 L254 310 L620 310 L620 354 L0 354 Z" fill="var(--orange)"/>
    <path d="M0 336 L216 336 L248 302 L620 302" fill="none" stroke="var(--white)" stroke-width="3"/>
  </svg>
  <div class="wordmark">Brindle<br>Earthworks</div>
  <div class="brand"><span class="brand__square"></span><span>Brindle Earthworks</span></div>

  <div class="person">
    <p class="person__name">Rowan Hale</p>
    <p class="person__role">Managing Director</p>
    <ul class="person__lines">
      <li class="person__line">
        <svg width="12" height="12" viewBox="0 0 16 16" aria-hidden="true"><path d="M4 1l3 4-2 2c1 2 2 3 4 4l2-2 4 3-2 3C7 15 1 9 1 3z" fill="var(--orange)"/></svg>
        03 5550 1824
      </li>
      <li class="person__line">
        <svg width="12" height="12" viewBox="0 0 16 16" aria-hidden="true"><rect x="4" y="1" width="8" height="14" rx="1.5" fill="none" stroke="var(--orange)" stroke-width="1.8"/></svg>
        02 5550 7391
      </li>
      <li class="person__line">
        <svg width="12" height="12" viewBox="0 0 16 16" aria-hidden="true"><rect x="1" y="3" width="14" height="10" fill="var(--orange)"/><path d="M1 3l7 6 7-6" fill="none" stroke="var(--card)" stroke-width="1.5"/></svg>
        admin@brindleearthworks-example.com.au
      </li>
    </ul>
  </div>

  <div class="address">
    <p>14 Ridgeback Road<br>Tallowvale Victoria 3799<br>Australia</p>
    <svg width="12" height="16" viewBox="0 0 12 16" aria-hidden="true"><path d="M6 0a6 6 0 0 1 6 6c0 4-6 10-6 10S0 10 0 6a6 6 0 0 1 6-6z" fill="var(--orange)"/><circle cx="6" cy="6" r="2.2" fill="var(--card)"/></svg>
  </div>

  <div class="web">
    <svg width="14" height="14" viewBox="0 0 16 16" aria-hidden="true"><g fill="none" stroke="var(--ink)" stroke-width="1.5"><circle cx="8" cy="8" r="6.5"/><ellipse cx="8" cy="8" rx="3" ry="6.5"/><path d="M1.5 8h13"/></g></svg>
    brindleearthworks-example.com.au
  </div>
</section>

</body>
</html>
```